The Lantern Harbor Summit (Poster or Color Flyer)

Unique and not too traditional design with Wording:
The Lantern Harbor Summit: The Deeper Message of God's Relentless Love
Friday Aug. 5 - Sunday the 7th
Denver 2016
www.TheLanternSummit.example
Updates
Project Deadline Extended
Reason: Our first experience with this type of design service was with 47Pixel, and we received 140 designs within a week.
We received only 2 designers submissions by our first 5 days with Mosaic Bench. We received an email that our time would be extended, which is much appreciated. The last 24 hours has brought in several new designs - which is great. However, we have a team of reviewers on our end - and due to Christmas break, will not be able to make a decision until January 4 or 5.
Can our deadline be moved to January 5? (at no charge?)
THANKS,
Trevor
Target Market(s)
General public. Professors. Pastors.
Requirements
Must have
- Basic info above.
Nice to have
- Subtle verses tucked into the graphics
- See www.TheQKTs.example for some of these,
- such as Romans 11:32, 1 John 2:2, 1 Timothy 4:10, John 12:32
Should not have
- Typical religious appearance.

```html
<!DOCTYPE html>
<html lang="en">
<head>
<meta charset="utf-8">
<title>The Lantern Harbor Summit</title>
<link rel="stylesheet" href="https://fonts.googleapis.com/css2?family=Montserrat:wght@500;700;800&family=Open+Sans:wght@700&display=swap">
<style>
  :root {
    --night-deep: #05071a;
    --night-mid: #12163d;
    --night-violet: #2a1a4f;
    --ink-white: #ffffff;
    --shadow-black: #000000;
    --verse-grey: #8a90b4;
    --orb-violet: rgba(150, 40, 150, 0.38);
    --orb-green: rgba(30, 110, 90, 0.45);
    --orb-magenta: rgba(120, 20, 110, 0.5);
    --orb-teal: rgba(20, 110, 110, 0.45);
  }
  * { margin: 0; padding: 0; box-sizing: border-box; }
  html, body { width: 848px; height: 1200px; overflow: hidden; background: var(--night-deep); }
  .poster {
    position: relative;
    width: 848px;
    height: 1200px;
    overflow: hidden;
    background:
      radial-gradient(ellipse 60% 45% at 45% 50%, var(--night-violet) 0%, transparent 70%),
      radial-gradient(ellipse 70% 40% at 50% 0%, var(--night-mid) 0%, transparent 80%),
      linear-gradient(180deg, #0a0d2a 0%, var(--night-deep) 55%, #080a22 100%);
    font-family: "Montserrat", sans-serif;
    color: var(--ink-white);
  }
  .orbs { position: absolute; inset: 0; }
  .figure-art {
    position: absolute;
    left: 190px; top: 300px;
    width: 460px; height: 690px;
    border-radius: 45% 45% 40% 40%;
    background: radial-gradient(ellipse 40% 50% at 50% 40%, rgba(200, 170, 230, 0.55) 0%, rgba(140, 110, 200, 0.3) 45%, transparent 75%);
  }
  .title {
    position: absolute;
    top: 22px; left: 0; width: 100%;
    text-align: center;
    font-weight: 800;
    font-size: 62px;
    line-height: 84px;
    letter-spacing: 1px;
    text-transform: uppercase;
    text-shadow: 5px 5px 0 var(--shadow-black);
  }
  .dots {
    position: absolute;
    height: 0;
    border-top: 6px dotted var(--ink-white);
  }
  .dots--top { top: 210px; left: 40px; width: 768px; }
  .dots--mid { top: 968px; left: 40px; width: 768px; border-top-width: 4px; }
  .dots--low { top: 1100px; left: 80px; width: 688px; border-top-width: 4px; }
  .subtitle {
    position: absolute;
    top: 228px; left: 0; width: 100%;
    text-align: center;
    font-weight: 700;
    font-size: 27px;
    text-transform: uppercase;
    text-shadow: 3px 3px 0 var(--shadow-black);
  }
  .verse {
    position: absolute;
    font-family: "Open Sans", sans-serif;
    font-weight: 700;
    font-size: 15px;
    line-height: 21px;
    text-transform: uppercase;
    color: var(--verse-grey);
  }
  .verse cite {
    display: block;
    font-style: normal;
    font-size: 8px;
    line-height: 14px;
    margin-top: 2px;
  }
  .verse--top-left { left: 42px; top: 352px; width: 320px; }
  .verse--top-right { right: 36px; top: 365px; width: 300px; text-align: right; }
  .verse--top-right cite { margin-top: 12px; }
  .verse--bottom-left { left: 42px; top: 746px; width: 320px; }
  .verse--bottom-left cite { margin-top: 10px; }
  .verse--bottom-right { right: 48px; top: 822px; width: 300px; text-align: right; }
  .event-dates {
    position: absolute;
    top: 982px; left: 0; width: 100%;
    text-align: center;
    font-weight: 500;
    font-size: 47px;
    line-height: 56px;
    text-transform: uppercase;
  }
  .event-url {
    position: absolute;
    top: 1130px; left: 0; width: 100%;
    text-align: center;
    font-weight: 500;
    font-size: 27px;
    text-transform: uppercase;
  }
</style>
</head>
<body>
<main class="poster">
  <svg class="orbs" width="848" height="1200" viewBox="0 0 848 1200" aria-hidden="true">
    <circle cx="415" cy="350" r="110" fill="var(--orb-violet)"/>
    <circle cx="305" cy="495" r="105" fill="var(--orb-green)"/>
    <circle cx="555" cy="650" r="148" fill="var(--orb-magenta)"/>
    <circle cx="345" cy="815" r="110" fill="var(--orb-teal)"/>
  </svg>

  <div class="figure-art" role="img" aria-label="Glowing translucent human figure rising with arms open against a starry cosmic sky"></div>

  <h1 class="title">The Lantern Harbor<br>Summit:</h1>
  <div class="dots dots--top"></div>
  <p class="subtitle">The Deeper Message of God's Relentless Love</p>

  <p class="verse verse--top-left">For God has consigned all to disobedience so that he may have mercy on them all.<cite>Romans 11:32</cite></p>
  <p class="verse verse--top-right">He is the atoning sacrifice for our sins, and not only for ours but also for the sins of the whole world.<cite>1 John 2:2</cite></p>
  <p class="verse verse--bottom-left">That is why we labor because we trust in the living God who is the Savior of all men, especially those who believe.<cite>1 Timothy 4:10</cite></p>
  <p class="verse verse--bottom-right">And we have seen and testify that the Father has sent his Son to be the Savior of the world.<cite>John 12:32</cite></p>

  <div class="dots dots--mid"></div>
  <p class="event-dates">Friday Aug. 5 - Sunday the 7th<br>Denver 2016</p>
  <div class="dots dots--low"></div>
  <p class="event-url">www.TheLanternSummit.example</p>
</main>
</body>
</html>
```